3846 Kell Lane (Rental house) with ONLINE APPLICATION

One home for rent. Would like to display pictures of the property and allow the candidates to apply online via the website. The application for the tenants must be able to be edited if I wish to change the questions, delete a question, or add a new one. I would also like to use Coinvex to charge the candidates a fee to apply to rent the property. Most of the website will be photos displaying the property. But also need to include some basic property details, contact info and the above mentioned application process. I've included a website that I like, but please bring your own ideas!
Business Name can be: 3846 Kell Lane
Contact Name: Delia Marston
Contact Number: (225) 555-0193

Target Market(s)

People who want to rent a house

Industry/Entity Type

Real Estate

Font styles to use
Serif

Colors
3176b5

Requirements
Must have
• #1 - Data collection for the application. See above. And also a way to view / print the inputted data.
• #2 - Great photo gallery
• #3 - Ability to edit the application questions and create new ones if I need to.
• #4 - Ability to edit the pictures
Nice to have
• A great photo slideshow viewer

```html
<!DOCTYPE html>
<html lang="en">
<head>
<meta charset="utf-8">
<title>3846 Kell Lane – Home for Rent</title>
<link href="https://fonts.googleapis.com/css2?family=Open+Sans:wght@400;600;700&family=Raleway:wght@300;400;600;700&display=swap" rel="stylesheet">
<style>
:root{
  --navy:#262a5f;
  --navy-deep:#1e2150;
  --orange:#f5ab2f;
  --brown:#8a5a2b;
  --price:#c7a27a;
  --ink:#3a3a3a;
  --muted:#888888;
  --line:#e4e4e4;
  --paper:#ffffff;
  --footer:#efefef;
}
*{box-sizing:border-box;margin:0;padding:0}
html,body{width:1200px;height:2848px;overflow:hidden;background:var(--paper)}
body{font-family:"Open Sans",Arial,sans-serif;color:var(--ink);position:relative}

/* header */
.site-header{position:absolute;left:0;top:0;width:1200px;height:128px;background:#fff}
.brand{position:absolute;left:86px;top:30px;display:flex;align-items:center;gap:10px;font-family:"Raleway",sans-serif;font-weight:700;font-size:30px;color:var(--navy);white-space:nowrap}
.brand-mark{width:34px;height:34px;background:var(--navy)}
.socials{position:absolute;left:676px;top:22px;display:flex;gap:14px}
.socials span{width:30px;height:30px;border-radius:50%;background:var(--brown)}
.call{position:absolute;left:880px;top:22px;font-family:"Raleway",sans-serif;font-size:24px;color:var(--navy);font-weight:600;white-space:nowrap}
.main-nav{position:absolute;left:550px;top:84px;display:flex}
.main-nav a{display:block;padding:8px 22px;font-size:15px;color:var(--ink);text-decoration:none;font-weight:600;letter-spacing:.5px}
.main-nav a.active{border-bottom:3px solid var(--orange)}

/* hero */
.hero{position:absolute;left:0;top:128px;width:1200px;height:588px;overflow:hidden}
.hero-photo{position:absolute;inset:0;background:linear-gradient(180deg,#9fb6d6 0%,#c9d3e3 38%,#6f7a92 62%,#3a3b45 100%)}
.hero-panel{position:absolute;left:680px;top:0;width:520px;height:588px;background:rgba(38,42,95,.93);color:#fff;padding:58px 40px 0 30px}
.hero-panel h1{font-family:"Raleway",sans-serif;font-size:30px;font-weight:700;margin-bottom:18px}
.hero-panel p{font-size:17px;line-height:1.5;color:#dfe0ee;margin-bottom:30px}
.btn-brown{display:inline-block;background:var(--brown);color:#fff;font-size:14px;padding:12px 28px}
.hero-features{display:flex;justify-content:space-between;margin-top:70px;width:360px;margin-left:30px}
.hero-features div{text-align:center;font-size:14px;color:#fff}
.hero-features svg{display:block;margin:0 auto 8px}
.hero-price{margin-top:40px;border-top:1px solid rgba(255,255,255,.25);padding-top:38px;text-align:center;font-family:"Raleway",sans-serif;font-size:44px;color:var(--price);width:420px}
.hero-price small{font-size:20px}
.slider-ctrl{position:absolute;left:120px;top:474px;width:92px;height:36px;background:#16161c;display:flex;justify-content:space-between;align-items:center;padding:0 10px}

/* quick application band */
.apply-band{position:absolute;left:0;top:720px;width:1200px;height:168px;background:var(--orange)}
.apply-input{position:absolute;left:100px;top:30px;width:820px;height:40px;background:#fff;font-size:13px;color:#aaa;padding:11px 14px}
.apply-btn{position:absolute;left:940px;top:30px;width:148px;height:40px;background:var(--navy);color:#fff;font-size:14px;text-align:center;line-height:40px}
.apply-opts{position:absolute;left:100px;top:92px;display:flex;gap:18px;align-items:center;font-size:12px;color:#fff}
.apply-opts .chk{display:flex;align-items:center;gap:6px}
.apply-opts .chk i{width:12px;height:12px;background:#fff}
.select{width:150px;height:34px;background:#fff;color:#999;padding:9px 10px;font-size:12px}

/* gallery */
.section-title{position:absolute;left:108px;font-size:14px;font-weight:600;color:#555;letter-spacing:.5px;text-transform:uppercase;width:984px;border-bottom:1px solid var(--line);padding-bottom:10px}
.card{position:absolute;width:256px}
.card-photo{height:152px}
.card h3{font-size:12px;font-weight:600;color:#666;margin:12px 0 8px;letter-spacing:.5px}
.card-meta{display:flex;justify-content:space-between;align-items:center;border-top:1px solid var(--line);border-bottom:1px solid var(--line);padding:8px 0;font-size:11px;color:#777}
.card p{font-size:12px;line-height:1.6;color:var(--muted);margin:12px 0}
.btn-navy{display:inline-block;background:var(--navy);color:#fff;font-size:12px;padding:6px 14px}
.photo-room{background:linear-gradient(135deg,#5a3a26,#a76a3e 55%,#e2b98b)}
.photo-warm{background:linear-gradient(135deg,#6d4227,#c0814a 50%,#f0d0a6)}
.photo-board{background:linear-gradient(135deg,#8a4a3a,#3f6b55 55%,#9fb7a5)}

/* application */
.application{position:absolute;left:108px;top:2008px;width:984px;height:400px;display:flex}
.app-item{width:492px;display:flex}
.app-photo{width:286px;height:400px}
.app-text{width:206px;height:400px;padding:52px 22px;color:#fff}
.app-text h4{font-family:"Raleway",sans-serif;font-size:17px;font-weight:600;letter-spacing:.5px;margin-bottom:6px}
.app-text .by{font-size:12px;opacity:.85;margin-bottom:24px}
.app-text p{font-size:12px;line-height:1.7;margin-bottom:22px}
.app-text .link{font-size:12px}
.bg-orange{background:var(--orange)}
.bg-navy{background:var(--navy)}
.photo-office{background:linear-gradient(160deg,#f4f4f4,#c9c9c9 60%,#8e8e8e)}
.photo-desk{background:linear-gradient(160deg,#f1f1f1,#bdbdbd 55%,#6e6e6e)}

/* footer */
.site-footer{position:absolute;left:0;top:2480px;width:1200px;height:332px;background:var(--footer)}
.footer-brand{position:absolute;left:100px;top:58px;font-family:"Raleway",sans-serif;font-weight:300;font-size:46px;color:#555;white-space:nowrap}
.footer-about{position:absolute;left:100px;top:128px;width:420px;font-size:12px;line-height:1.6;color:var(--muted)}
.footer-about .btn-brown{margin-top:14px;padding:7px 20px;font-size:12px}
.footer-col h5{font-size:14px;font-weight:600;color:#555;margin-bottom:12px;padding-bottom:6px;border-bottom:1px solid #d5d5d5}
.footer-col li{list-style:none;font-size:11px;color:var(--muted);line-height:1.9}
.footer-menu{position:absolute;left:540px;top:70px;width:100px}
.footer-address{position:absolute;left:690px;top:70px;width:210px}
.addr-row{display:flex;gap:8px;font-size:11px;color:#777;margin-bottom:10px;align-items:flex-start}
.addr-row i{width:12px;height:12px;border-radius:50%;background:#777;flex:none;margin-top:2px}
.f-socials{display:flex;gap:8px;margin-top:8px}
.f-socials span{width:22px;height:22px;border-radius:50%;background:#8a8a8a}
.map{position:absolute;left:912px;top:64px;width:200px;height:150px;background:linear-gradient(135deg,#e3e6ea,#cfd6de)}
.footer-bar{position:absolute;left:0;top:2812px;width:1200px;height:36px;background:var(--navy-deep);color:#c8cae0;font-size:11px;line-height:36px;text-align:center}
</style>
</head>
<body>

<header class="site-header">
  <div class="brand"><span class="brand-mark"></span>3846 Kell Lane</div>
  <div class="socials"><span></span><span></span><span></span><span></span></div>
  <div class="call">Call us now : (225) 555-0193</div>
  <nav class="main-nav">
    <a class="active">HOME</a><a>GALLERY</a><a>DETAILS</a><a>APPLY</a><a>CONTACT</a>
  </nav>
</header>

<section class="hero">
  <div class="hero-photo" role="img" aria-label="Front view of the two-storey house at 3846 Kell Lane at dusk"></div>
  <div class="slider-ctrl">
    <svg width="12" height="14"><path d="M9 2L3 7l6 5" stroke="#fff" stroke-width="2" fill="none"/></svg>
    <svg width="12" height="14"><path d="M3 2l6 5-6 5" stroke="#fff" stroke-width="2" fill="none"/></svg>
  </div>
  <div class="hero-panel">
    <h1>Family Home for Rent</h1>
    <p>A bright two-storey house with a garage, garden and quiet street. Browse the photos and apply online in minutes.</p>
    <span class="btn-brown">Apply Now</span>
    <div class="hero-features">
      <div><svg width="26" height="22"><rect x="2" y="8" width="22" height="10" fill="none" stroke="#fff" stroke-width="2"/><path d="M2 18v3M24 18v3" stroke="#fff" stroke-width="2"/></svg>3 Bedrooms</div>
      <div><svg width="26" height="22"><path d="M3 14h20v4H3zM5 14V6h6v8" fill="none" stroke="#fff" stroke-width="2"/></svg>2 Baths</div>
      <div><svg width="26" height="22"><rect x="4" y="3" width="18" height="16" fill="none" stroke="#fff" stroke-width="2"/><path d="M4 11h18" stroke="#fff" stroke-width="2"/></svg>1,850 ft²</div>
    </div>
    <div class="hero-price">$ 1,450 <small>/ month</small></div>
  </div>
</section>

<section class="apply-band">
  <div class="apply-input">Enter your full name to start an application...</div>
  <div class="apply-btn">Start</div>
  <div class="apply-opts">
    <span class="chk"><i></i>6 mo</span>
    <span class="chk"><i></i>12 mo</span>
    <span class="chk"><i></i>Pets</span>
    <span class="select">Move-in date</span>
    <span class="select">Occupants</span>
    <span class="select">Income</span>
    <span class="select">Email</span>
  </div>
</section>

<h2 class="section-title" style="top:928px">Photo Gallery - Living Spaces</h2>

<article class="card" style="left:108px;top:1000px">
  <div class="card-photo photo-room" role="img" aria-label="Living room with brick wall"></div>
  <h3>LIVING ROOM</h3>
  <div class="card-meta"><span>&#8962;</span><span>18 x 16 ft</span></div>
  <p>Open living room with exposed brick, wide windows and warm oak floors.</p>
  <span class="btn-navy">View photos</span>
</article>
<article class="card" style="left:472px;top:1000px">
  <div class="card-photo photo-warm" role="img" aria-label="Kitchen and dining area in warm wood"></div>
  <h3>KITCHEN &amp; DINING</h3>
  <div class="card-meta"><span>&#8962;</span><span>20 x 14 ft</span></div>
  <p>Updated kitchen with new appliances, pantry and a sunny dining nook.</p>
  <span class="btn-navy">View photos</span>
</article>
<article class="card" style="left:836px;top:1000px">
  <div class="card-photo photo-board" role="img" aria-label="Study with brick wall and green board"></div>
  <h3>STUDY</h3>
  <div class="card-meta"><span>&#8962;</span><span>12 x 10 ft</span></div>
  <p>Quiet study off the hall, ideal as a home office or reading room.</p>
  <span class="btn-navy">View photos</span>
</article>

<h2 class="section-title" style="top:1420px">Photo Gallery - Bedrooms &amp; Outdoors</h2>

<article class="card" style="left:108px;top:1492px">
  <div class="card-photo photo-room" role="img" aria-label="Main bedroom"></div>
  <h3>MAIN BEDROOM</h3>
  <div class="card-meta"><span>&#8962;</span><span>16 x 14 ft</span></div>
  <p>Spacious main bedroom with walk-in closet and private bathroom.</p>
  <span class="btn-navy">View photos</span>
</article>
<article class="card" style="left:472px;top:1492px">
  <div class="card-photo photo-warm" role="img" aria-label="Guest bedroom"></div>
  <h3>GUEST BEDROOMS</h3>
  <div class="card-meta"><span>&#8962;</span><span>12 x 12 ft</span></div>
  <p>Two bright guest rooms upstairs sharing a full hall bathroom.</p>
  <span class="btn-navy">View photos</span>
</article>
<article class="card" style="left:836px;top:1492px">
  <div class="card-photo photo-board" role="img" aria-label="Back garden and patio"></div>
  <h3>GARDEN &amp; PATIO</h3>
  <div class="card-meta"><span>&#8962;</span><span>Fenced yard</span></div>
  <p>Fenced back garden with a covered patio and a two-car garage.</p>
  <span class="btn-navy">View photos</span>
</article>

<h2 class="section-title" style="top:1960px">Online Application</h2>

<section class="application">
  <div class="app-item">
    <div class="app-photo photo-office" role="img" aria-label="Bright entry hall of the house"></div>
    <div class="app-text bg-orange">
      <h4>APPLY ONLINE</h4>
      <div class="by">Step 1 of 2</div>
      <p>Fill in the rental form with your details, work history and references. You can save it and return later.</p>
      <div class="link">&#10148; Open the form</div>
    </div>
  </div>
  <div class="app-item">
    <div class="app-photo photo-desk" role="img" aria-label="Modern study with desk and lamp"></div>
    <div class="app-text bg-navy">
      <h4>APPLICATION FEE</h4>
      <div class="by">Step 2 of 2</div>
      <p>Pay the $35 fee securely with Coinvex. Your application is sent once the payment is complete.</p>
      <div class="link">&#10148; Pay with Coinvex</div>
    </div>
  </div>
</section>

<footer class="site-footer">
  <div class="footer-brand">3846 Kell Lane</div>
  <div class="footer-about">
    A well kept family home offered for long-term rent. Questions about the house, viewings or the application? Contact Delia Marston by phone or message and we will reply within one business day.
    <br><span class="btn-brown">Apply now</span>
  </div>
  <div class="footer-col footer-menu">
    <h5>Menu</h5>
    <ul><li>HOME</li><li>GALLERY</li><li>DETAILS</li><li>APPLY</li><li>CONTACT</li></ul>
  </div>
  <div class="footer-col footer-address">
    <h5>Contact</h5>
    <div class="addr-row"><i></i><span>Delia Marston<br>3846 Kell Lane</span></div>
    <div class="addr-row"><i></i><span>(225) 555-0193</span></div>
    <div class="f-socials"><span></span><span></span><span></span><span></span></div>
  </div>
  <div class="map" role="img" aria-label="Street map showing the location of 3846 Kell Lane"></div>
</footer>
<div class="footer-bar">Site Map &nbsp;|&nbsp; Privacy &nbsp;|&nbsp; Terms &nbsp;|&nbsp; &copy; 3846 Kell Lane All rights reserved.</div>

</body>
</html>
```